Business Card for a recruitment agency specializing in engineers and geeks.

I am looking to create Business Card Design for my company.
That
## Company name:
Quorvant Inc.
Quorvant is a term coined from the following concepts.
1. geek + engineer
2. geek utopia
## Company Description:
The concept of the company is to be a recruitment agency that creates a paradise for geeky engineers. We want to be a place where engineers can have more freedom and ideal career support.
# Target.
The noun itself is often given to companies that want to hire engineers, geeks, and IT-related personnel, so it would be nice to get the impression that this company seems to have good engineers and IT personnel. There are many occasions where I meet with the human resources department, president, or senior management and give it to them.
# Atmosphere
We are happy with simplicity, but with an impact that will help people remember the company. The logo is based on a dinosaur that does programming, so it should be somewhat playful, but since it will basically be used in a business setting, please don't make it too silly.
# About the logo
See the attached files. The company logo represents our engineers smiling upward because of our work, with the motif of a dinosaur doing programming.
## Color
We will leave the color scheme to you, but since the logo is in black and white, colors with such a taste would fit well.
## file format
ai, psd, png, svg
Industry/Entity Type
human resource and employment agency
Contact Information for Business Card
Company name, address, email, tel, URL,logo
Colors
Designer to choose colors to be used in the design.

```html
<!DOCTYPE html>
<html lang="en">
<head>
<meta charset="utf-8">
<title>Quorvant Business Card</title>
<link href="https://fonts.googleapis.com/css2?family=Montserrat:wght@400;500;700&display=swap" rel="stylesheet">
<style>
  :root {
    --page-bg: #f6f6f6;
    --card-top: #202020;
    --card-bottom: #1a1a1a;
    --ink: #ffffff;
    --ink-soft: #e9e9e9;
    --ghost: #262626;
    --shadow: rgba(0, 0, 0, 0.28);
  }
  * { margin: 0; padding: 0; box-sizing: border-box; }
  html, body {
    width: 800px;
    height: 1200px;
    overflow: hidden;
    background: var(--page-bg);
    font-family: "Montserrat", sans-serif;
  }
  .sheet {
    position: relative;
    width: 800px;
    height: 1200px;
  }
  .card {
    position: absolute;
    left: 90px;
    width: 620px;
    height: 354px;
    background: linear-gradient(160deg, var(--card-top), var(--card-bottom));
    box-shadow: 0 6px 18px var(--shadow);
    overflow: hidden;
    color: var(--ink);
  }
  .card--front { top: 214px; }
  .card--back { top: 598px; }

  /* Front */
  .mark-slot {
    position: absolute;
    left: 46px;
    top: 0;
    width: 242px;
    height: 354px;
    display: flex;
    align-items: center;
    justify-content: center;
    gap: 12px;
  }
  .mark-slot__square {
    width: 26px;
    height: 26px;
    background: var(--ink);
  }
  .mark-slot__name {
    font-weight: 700;
    font-size: 34px;
    color: var(--ink);
    letter-spacing: 0.5px;
  }
  .wordmark {
    position: absolute;
    left: 338px;
    top: 88px;
    font-weight: 500;
    font-size: 40px;
    line-height: 1;
    color: var(--ink);
  }
  .contact-list {
    position: absolute;
    left: 340px;
    top: 156px;
    list-style: none;
  }
  .contact-list__item {
    display: flex;
    align-items: flex-start;
    font-size: 14px;
    line-height: 16px;
    color: var(--ink-soft);
    margin-bottom: 9px;
  }
  .contact-list__item--address { margin-bottom: 14px; }
  .contact-list__icon {
    width: 10px;
    height: 10px;
    margin: 3px 12px 0 0;
    flex: none;
    fill: var(--ink);
  }

  /* Back */
  .ghost-name {
    position: absolute;
    left: -30px;
    top: 80px;
    font-weight: 700;
    font-size: 150px;
    line-height: 1;
    color: var(--ghost);
    white-space: nowrap;
  }
  .back-lockup {
    position: absolute;
    right: 62px;
    top: 196px;
    display: flex;
    flex-direction: column;
    align-items: center;
    gap: 26px;
  }
  .back-lockup__mark {
    display: flex;
    align-items: center;
    gap: 8px;
  }
  .back-lockup__square {
    width: 14px;
    height: 14px;
    background: var(--ink-soft);
  }
  .back-lockup__name {
    font-weight: 700;
    font-size: 18px;
    color: var(--ink-soft);
  }
  .back-lockup__wordmark {
    font-weight: 500;
    font-size: 29px;
    line-height: 1;
    color: var(--ink-soft);
  }
</style>
</head>
<body>
<main class="sheet">
  <section class="card card--front" aria-label="Card front">
    <div class="mark-slot">
      <span class="mark-slot__square"></span>
      <span class="mark-slot__name">Quorvant</span>
    </div>
    <h1 class="wordmark">Quorvant</h1>
    <ul class="contact-list">
      <li class="contact-list__item">
        <svg class="contact-list__icon" viewBox="0 0 10 10"><path d="M2 0.5 L3.6 2.6 L2.8 3.6 C3.4 5 4.8 6.4 6.3 7.2 L7.3 6.3 L9.5 7.9 L8.4 9.5 C4.3 9 1 5.7 0.5 1.6 Z"/></svg>
        +000-1234-5678
      </li>
      <li class="contact-list__item">
        <svg class="contact-list__icon" viewBox="0 0 10 10"><path d="M0.5 2 H9.5 V8.5 H0.5 Z" /><path d="M0.5 2 L5 5.6 L9.5 2" fill="none" stroke="#1d1d1d" stroke-width="1"/></svg>
        youremail@email.com
      </li>
      <li class="contact-list__item contact-list__item--address">
        <svg class="contact-list__icon" viewBox="0 0 10 10"><path d="M5 0.3 C7.2 0.3 8.6 1.9 8.6 3.8 C8.6 6.2 5 9.7 5 9.7 C5 9.7 1.4 6.2 1.4 3.8 C1.4 1.9 2.8 0.3 5 0.3 Z M5 2.4 A1.4 1.4 0 1 0 5 5.2 A1.4 1.4 0 1 0 5 2.4 Z" fill-rule="evenodd"/></svg>
        <span>123 Main Street<br>11th Floor, Some City</span>
      </li>
      <li class="contact-list__item">
        <svg class="contact-list__icon" viewBox="0 0 10 10"><circle cx="5" cy="5" r="4.3" fill="none" stroke="#fff" stroke-width="1"/><path d="M0.7 5 H9.3 M5 0.7 C3 3 3 7 5 9.3 M5 0.7 C7 3 7 7 5 9.3" fill="none" stroke="#fff" stroke-width="0.9"/></svg>
        quorvant.com
      </li>
    </ul>
  </section>

  <section class="card card--back" aria-label="Card back">
    <div class="ghost-name" aria-hidden="true">Quorvant</div>
    <div class="back-lockup">
      <div class="back-lockup__mark">
        <span class="back-lockup__square"></span>
        <span class="back-lockup__name">Quorvant</span>
      </div>
      <div class="back-lockup__wordmark">Quorvant</div>
    </div>
  </section>
</main>
</body>
</html>
```